Larkmoor Stationery Design Project

company name : Larkmoor General Trading LLC.
light watermark taken from the logo to cover almost the middle of the stationary..
logo is attached and an on going business card project is released on the same company name..
thanks
Reason: more time for more designs and to work with comfort..
Industry/Entity Type
Business
Colors
Designer to choose colors to be used in the design.
Look and feel
Each slider illustrates characteristics of the customer's brand and the style your logo design should communicate.

```html
<!DOCTYPE html>
<html lang="en">
<head>
<meta charset="utf-8">
<title>Larkmoor Int. Stationery</title>
<link rel="stylesheet" href="https://fonts.googleapis.com/css2?family=Lora:wght@400;700&display=swap">
<style>
  :root {
    --backdrop: #e9e7e4;
    --paper: #ffffff;
    --ink: #333333;
    --brand-grey: #5e5e60;
    --brand-blue: #1f6fb3;
    --band: #5a5a5c;
    --band-text: #f2f2f2;
    --rule: #c9c9c9;
    --watermark: #f0f0f2;
    --card-dark-1: #5b5b5d;
    --card-dark-2: #0e0e0e;
    --card-dark-text: #b9b9bb;
  }
  * { box-sizing: border-box; margin: 0; padding: 0; }
  html, body { width: 1029px; height: 1200px; overflow: hidden; }
  body {
    background: var(--backdrop);
    font-family: "Lora", Georgia, serif;
    color: var(--ink);
    position: relative;
  }

  .brand-name {
    font-family: "Lora", Georgia, serif;
    font-weight: 400;
    color: var(--brand-grey);
    letter-spacing: 1px;
    display: flex;
    align-items: center;
    gap: 8px;
    white-space: nowrap;
  }
  .brand-name .brand-dot {
    width: 10px; height: 10px; border-radius: 50%;
    background: var(--brand-blue);
    flex: none;
  }

  .watermark {
    position: absolute;
    font-family: "Lora", Georgia, serif;
    font-weight: 400;
    color: var(--watermark);
    white-space: nowrap;
    letter-spacing: 4px;
    pointer-events: none;
    z-index: 0;
  }

  /* Business cards */
  .card {
    position: absolute;
    top: 20px;
    width: 286px;
    height: 172px;
    border-radius: 8px;
    overflow: hidden;
    box-shadow: 0 2px 8px rgba(0,0,0,.18);
  }
  .card--back {
    left: 120px;
    background: linear-gradient(100deg, var(--card-dark-1), var(--card-dark-2) 70%);
    display: flex; align-items: center; justify-content: center;
  }
  .card--back .brand-name { color: var(--card-dark-text); font-size: 22px; }
  .card--back .brand-dot { background: var(--card-dark-text); }

  .card--front {
    left: 402px;
    background: var(--paper);
    display: flex; flex-direction: column; align-items: center;
  }
  .card--front .brand-name { font-size: 19px; margin-top: 38px; }
  .card-holder { margin-top: 16px; text-align: center; }
  .card-holder__name { font-size: 10px; font-weight: 700; color: var(--brand-blue); letter-spacing: .5px; }
  .card-holder__role { font-size: 7px; color: #666; margin-top: 1px; }
  .card-contacts { display: flex; margin-top: 12px; font-size: 8px; color: #444; }
  .card-contacts__col { padding: 0 14px; display: flex; flex-direction: column; gap: 3px; }
  .card-contacts__col + .card-contacts__col { border-left: 1px solid var(--rule); }
  .card-band {
    position: absolute; left: 0; right: 0; bottom: 0; height: 18px;
    background: var(--band); color: var(--band-text);
    font-size: 7px; text-align: center; line-height: 18px;
  }

  .contact-item { display: flex; align-items: center; gap: 5px; }
  .contact-item svg { flex: none; }

  /* Compliment slip */
  .slip {
    position: absolute;
    left: 20px; top: 226px;
    width: 300px; height: 900px;
    background: var(--paper);
    box-shadow: 0 2px 10px rgba(0,0,0,.16);
    overflow: hidden;
  }
  .slip .brand-name { position: absolute; left: 40px; top: 66px; font-size: 20px; z-index: 1; }
  .slip .watermark { font-size: 46px; left: 20px; top: 420px; }
  .slip__band {
    position: absolute; left: 0; right: 0; bottom: 0; height: 24px;
    background: var(--band); color: var(--band-text);
    font-size: 9px; text-align: center; line-height: 24px;
  }

  /* Letterhead */
  .letterhead {
    position: absolute;
    left: 340px; top: 226px;
    width: 668px; height: 960px;
    background: var(--paper);
    box-shadow: 0 2px 10px rgba(0,0,0,.16);
    overflow: hidden;
  }
  .letterhead .watermark { font-size: 64px; left: 150px; top: 470px; }
  .letterhead__header {
    position: absolute; left: 50px; right: 50px; top: 38px;
    display: flex; justify-content: space-between; align-items: flex-start;
    z-index: 1;
  }
  .letterhead .brand-name { font-size: 22px; margin-top: 44px; }
  .letterhead__contacts {
    border-left: 1px solid var(--rule);
    padding-left: 12px;
    font-size: 11px; color: #444;
    display: flex; flex-direction: column; gap: 3px;
  }
  .letter {
    position: absolute; left: 50px; right: 50px; top: 158px;
    font-size: 13.2px; line-height: 20px;
    z-index: 1;
  }
  .letter__date { text-align: right; }
  .letter__recipient strong { font-weight: 700; }
  .letter__body p { margin-top: 20px; text-align: justify; hyphens: auto; }
  .letter__signoff { margin-top: 40px; }
  .signature-area {
    width: 170px; height: 50px; margin: 2px 0 0 -12px;
    background: linear-gradient(90deg, #f1f1f1, #e4e4e4);
    border-radius: 4px;
  }
  .letter__signer { margin-top: 2px; }
  .letterhead__band {
    position: absolute; left: 0; right: 0; bottom: 0; height: 25px;
    background: var(--band); color: var(--band-text);
    font-size: 11px; text-align: center; line-height: 25px;
  }
</style>
</head>
<body>

<svg width="0" height="0" style="position:absolute">
  <defs>
    <symbol id="icon-phone" viewBox="0 0 12 12">
      <circle cx="6" cy="6" r="5.5" fill="#1f6fb3"/>
      <rect x="4" y="3" width="4" height="6" rx="1" fill="#fff"/>
    </symbol>
    <symbol id="icon-mail" viewBox="0 0 12 12">
      <circle cx="6" cy="6" r="5.5" fill="#1f6fb3"/>
      <rect x="3" y="4" width="6" height="4" fill="#fff"/>
      <path d="M3 4l3 2.2L9 4" fill="none" stroke="#1f6fb3" stroke-width=".8"/>
    </symbol>
    <symbol id="icon-web" viewBox="0 0 12 12">
      <circle cx="6" cy="6" r="5.5" fill="#1f6fb3"/>
      <circle cx="6" cy="6" r="3" fill="none" stroke="#fff" stroke-width="1"/>
    </symbol>
  </defs>
</svg>

<section class="card card--back">
  <div class="brand-name"><span class="brand-dot"></span>LARKMOOR INT.</div>
</section>

<section class="card card--front">
  <div class="brand-name"><span class="brand-dot"></span>LARKMOOR INT.</div>
  <div class="card-holder">
    <div class="card-holder__name">DANIEL REYES HOLT</div>
    <div class="card-holder__role">General Manager</div>
  </div>
  <div class="card-contacts">
    <div class="card-contacts__col">
      <span class="contact-item"><svg width="9" height="9"><use href="#icon-phone"/></svg>64.210.5537</span>
      <span class="contact-item"><svg width="9" height="9"><use href="#icon-phone"/></svg>64.210.7719</span>
    </div>
    <div class="card-contacts__col">
      <span class="contact-item"><svg width="9" height="9"><use href="#icon-mail"/></svg>info@larkmoorint.com</span>
      <span class="contact-item"><svg width="9" height="9"><use href="#icon-web"/></svg>www.larkmoorint.com</span>
    </div>
  </div>
  <div class="card-band">48 Harbour Lane, P.O. Box 512, Westbrook, B.C. V4R 1K8</div>
</section>

<section class="slip">
  <div class="brand-name"><span class="brand-dot"></span>LARKMOOR INT.</div>
  <div class="watermark" aria-hidden="true">LARKMOOR</div>
  <footer class="slip__band">48 Harbour Lane, P.O. Box 512, Westbrook, B.C. V4R 1K8</footer>
</section>

<article class="letterhead">
  <div class="watermark" aria-hidden="true">LARKMOOR INT.</div>
  <header class="letterhead__header">
    <div class="brand-name"><span class="brand-dot"></span>LARKMOOR INT.</div>
    <div class="letterhead__contacts">
      <span class="contact-item"><svg width="11" height="11"><use href="#icon-phone"/></svg>64.210.5537</span>
      <span class="contact-item"><svg width="11" height="11"><use href="#icon-phone"/></svg>64.210.7719</span>
      <span class="contact-item"><svg width="11" height="11"><use href="#icon-mail"/></svg>info@larkmoorint.com</span>
      <span class="contact-item"><svg width="11" height="11"><use href="#icon-web"/></svg>www.larkmoorint.com</span>
    </div>
  </header>

  <div class="letter">
    <p class="letter__date">October 30, 2014</p>
    <p class="letter__recipient"><strong>Owen Pratt</strong><br>General Manager<br>Northfield Supply Co.</p>
    <div class="letter__body">
      <p>Lorem ipsum dolor sit amet, consectetur adipiscing elit. Donec orci purus, luctus vitae dignissim eu, iaculis sed purus. Vivamus faucibus, ipsum nec aliquet viverra, leo mauris condimentum ligula, sit amet sagittis enim ligula quis arcu. Nam egestas tortor id nisi porttitor mattis. In tortor ante, ultricies in suscipit a, tempus non massa.</p>
      <p>Quisque scelerisque sagittis nulla at porttitor. Mauris a justo et tellus interdum tristique. Sed id augue vitae urna euismod commodo aliquet a quam. Pellentesque arcu velit, cursus et malesuada ut, rutrum nisi iaculis consequat et diam. Nullam erat sem, rhoncus id ullamcorper vitae, rhoncus et arcu. In ultricies ultricies nulla, ut rutrum nisi iaculis at. Donec eu magna a metus ornare faucibus. Fusce aliquet faucibus ultricies. Morbi semper, est id tincidunt gravida, sem arcu adipiscing lacus, ac bibendum nulla leo eu purus. Quisque nec diam sed risus consectetur a ccumsan quis quis nibh. Vestibulum id purus lorem.</p>
      <p>Vivamus et auctor mi. Fusce vel massa nulla. Phasellus nec eros mauris, et scelerisque orci. Donec malesuada orci vitae nulla accumsan porta a id massa. Quisque accumsan iaculis magna sit amet fringilla. Maecenas consequat, magna eget tincidunt semper, odio nibh rutrum mi, id feugiat ante nisi eu risus. Vestibulum nunc orci, ultricies in mi. Quisque scelerisque sagittis nulla at porttitor. Mauris a justo et tellus interdum tristique. Sed id augue vitae urna euismod commodo lorem ipsum aliquet a quam.</p>
    </div>
    <p class="letter__signoff">Keep moving forward!</p>
    <div class="signature-area" role="img" aria-label="Handwritten signature of Daniel Reyes Holt"></div>
    <p class="letter__signer">Daniel Reyes Holt</p>
  </div>

  <footer class="letterhead__band">48 Harbour Lane, P.O. Box 512, Westbrook, B.C. V4R 1K8</footer>
</article>

</body>
</html>
```